Wholesale company needs a sales brochure for our latest gadget- Nimbo Pebble. We sell to retailers

We need a sale brochure for our new product- Nimbo/Dart Pebble. It's an elegant little device that connects to any smartphone using an APP and let you locate your keys or your phone when you can't find them. We would like to see a design that uses the colors: Light blue, Black and metallic silver. The final design should communicate tech and innovative product. We need a total of 4 pages of 8.5x11'' (US letter size) to describe:
- Product benefits
- Product in use
- Display solution
- Profit generator
- Success story

Attached below are photos of the packaging and the display for your reference. Better photos will be sent later.
Please keep in mind that this product should be displayed on the counter with high foot traffic OR hang on hooks on a display fixture in the store.

This brochure will be used mainly to be sent digitally via email BUT we will also print it and will be mailing copies to our buyers.

Target Market(s)

Retailers and Distributors.
Small to mid-size retail stores:
- Electronic stores
- Convenient store
- Cellphone stores
- Gift stores

Industry/Entity Type

Retail

Font styles to use
Sans Serif

Colors
0692cd
ffffff
f3f1f8
33a6d7
85cae6

Requirements
Must have
• Must have:
• - "techie" and innovative look to go hand in hand with the product itself.
• - "in use" photos
• - "Description of the product"
• - Spec info
Nice to have
• Pattern or abstract design on background behind the text and images

```html
<!DOCTYPE html>
<html lang="en">
<head>
<meta charset="utf-8">
<title>Sales Brochure – Spread</title>
<link rel="stylesheet" href="https://fonts.googleapis.com/css2?family=Roboto:wght@300;400;700&display=swap">
<style>
  :root {
    --blue: #0692cd;
    --blue-mid: #33a6d7;
    --blue-light: #85cae6;
    --white: #ffffff;
    --paper: #f3f1f8;
    --stage: #e4e4e6;
    --ink: #111111;
    --body: #555559;
    --silver-1: #c9c9cd;
    --silver-2: #ededef;
    --page-grey: #ececee;
    --phone-dark: #2a2a2d;
  }
  * { box-sizing: border-box; margin: 0; padding: 0; }
  html, body { width: 1200px; height: 833px; overflow: hidden; }
  body {
    background: var(--stage);
    font-family: "Roboto", Arial, sans-serif;
    color: var(--body);
  }
  .spread {
    position: absolute;
    left: 44px; top: 56px;
    width: 1112px; height: 720px;
    display: flex;
    box-shadow: 0 10px 30px rgba(0,0,0,.12);
  }
  .page {
    position: relative;
    width: 556px; height: 720px;
    background: var(--white);
    overflow: hidden;
  }
  .page--left { background: linear-gradient(160deg, var(--page-grey), #f6f6f7); }
  .page--right { background: linear-gradient(90deg, #f0f0f2 0, var(--white) 40px); }
  .page--left::after {
    content: ""; position: absolute; top: 0; right: 0; width: 30px; height: 100%;
    background: linear-gradient(90deg, transparent, rgba(0,0,0,.06));
  }

  .section-title {
    position: absolute;
    font-weight: 300;
    font-size: 19px;
    color: var(--blue);
  }
  .copy { position: absolute; font-size: 8.5px; line-height: 1.45; }
  .copy p + p { margin-top: 7px; }

  .benefit { position: absolute; width: 110px; text-align: center; }
  .benefit__icon {
    width: 72px; height: 72px; margin: 0 auto 8px;
    border-radius: 50%; background: var(--blue-mid);
    display: flex; align-items: center; justify-content: center;
  }
  .item-title { font-weight: 700; font-size: 11px; color: var(--ink); margin-bottom: 4px; }
  .item-text { font-size: 7.5px; line-height: 1.4; }

  .hero-device {
    position: absolute; left: 0; bottom: 0; width: 370px; height: 150px;
    background: linear-gradient(180deg, var(--silver-2), var(--silver-1));
  }

  .solution { position: absolute; top: 80px; width: 130px; text-align: center; }
  .solution__device {
    width: 96px; height: 170px; margin: 0 auto 12px;
    border-radius: 16px;
    background: linear-gradient(180deg, #46464a, var(--phone-dark) 55%, #18181a);
  }

  .profit-photo {
    position: absolute; left: 40px; top: 410px; width: 476px; height: 270px;
    background: linear-gradient(135deg, #0a5f8a, var(--blue) 55%, var(--blue-mid));
  }
  .profit-copy {
    position: absolute; left: 62px; top: 440px; width: 430px;
    color: var(--white); font-size: 9px; line-height: 1.5;
  }
  .profit-copy p + p { margin-top: 8px; }
</style>
</head>
<body>
<main class="spread">
  <section class="page page--left">
    <h2 class="section-title" style="left:46px; top:48px;">Product benefits</h2>
    <div class="copy" style="left:46px; top:78px; width:440px;">
      <p>A small tag clips to any key ring and pairs with your phone in seconds through a free app, so lost keys ring out loud when you need them.</p>
      <p>Press the tag to find your phone, even on silent mode.</p>
    </div>

    <div class="benefit" style="left:66px; top:220px;">
      <div class="benefit__icon">
        <svg width="32" height="32" viewBox="0 0 32 32" aria-hidden="true"><path d="M7 16l6 6 12-13" fill="none" stroke="#fff" stroke-width="3" stroke-linecap="round" stroke-linejoin="round"/></svg>
      </div>
      <div class="item-title">benefit one</div>
      <p class="item-text">Tap the app and the tag chimes loudly, guiding you straight to your keys in any room.</p>
    </div>
    <div class="benefit" style="left:216px; top:172px;">
      <div class="benefit__icon">
        <svg width="32" height="32" viewBox="0 0 32 32" aria-hidden="true"><path d="M7 16l6 6 12-13" fill="none" stroke="#fff" stroke-width="3" stroke-linecap="round" stroke-linejoin="round"/></svg>
      </div>
      <div class="item-title">benefit two</div>
      <p class="item-text">Press the tag once and your phone rings, even when it sits on silent under a cushion.</p>
    </div>
    <div class="benefit" style="left:366px; top:130px;">
      <div class="benefit__icon">
        <svg width="32" height="32" viewBox="0 0 32 32" aria-hidden="true"><path d="M7 16l6 6 12-13" fill="none" stroke="#fff" stroke-width="3" stroke-linecap="round" stroke-linejoin="round"/></svg>
      </div>
      <div class="item-title">benefit three</div>
      <p class="item-text">A slim shell and a long life battery keep it working for a full year without charging.</p>
    </div>

    <h2 class="section-title" style="left:46px; top:392px;">Product in use</h2>
    <div class="copy" style="left:46px; top:422px; width:450px;">
      <p>Shoppers clip the tag to keys, bags or wallets and link it to any smartphone through one simple app with no account needed.</p>
      <p>When keys go missing, a tap in the app sets off a clear tone. The app also marks the last place the tag was seen on a map.</p>
      <p>Range up to 30 metres, tone at 85 dB, battery life of twelve months.</p>
    </div>

    <div class="hero-device" role="img" aria-label="Photo of a silver smartphone lying on its side"></div>
  </section>

  <section class="page page--right">
    <h2 class="section-title" style="left:40px; top:46px;">Display solution</h2>

    <div class="solution" style="left:40px;">
      <div class="solution__device" role="img" aria-label="Photo of a smartphone showing the finder app"></div>
      <div class="item-title">solution one</div>
      <p class="item-text">A compact counter box holds twelve units right beside the till for impulse buys.</p>
    </div>
    <div class="solution" style="left:213px;">
      <div class="solution__device" role="img" aria-label="Photo of a smartphone showing the finder app"></div>
      <div class="item-title">solution two</div>
      <p class="item-text">Blister cards hang on standard peg hooks and fit any wall or gondola fixture.</p>
    </div>
    <div class="solution" style="left:386px;">
      <div class="solution__device" role="img" aria-label="Photo of a smartphone showing the finder app"></div>
      <div class="item-title">solution three</div>
      <p class="item-text">A floor stand with header card shows off the whole range in busy aisles.</p>
    </div>

    <h2 class="section-title" style="left:40px; top:378px;">Profit generator</h2>
    <div class="profit-photo" role="img" aria-label="Blue-toned photo of a laptop showing a sales chart"></div>
    <div class="profit-copy">
      <p>Priced as a low cost add on, the tag sells fast next to phone cases, chargers and gift items at the counter.</p>
      <p>Retailers earn strong margins on every unit sold, and repeat buys follow as shoppers come back for extra tags for family members.</p>
      <p>Ask us about volume pricing and free display units.</p>
    </div>
  </section>
</main>
</body>
</html>
```